Church Website with Home Page and Member Sermon Library

I am in need of an updated design for our church website. This will include 4 pages (outlined below). We are a conservative, evangelical, Christian church. The site should be modern and clean, while still reflecting our conservative values. I already have a logo for our church, and I want the site to incorporate the logo, and match the logo/branding. Stock photos are allowed if needed, but I have uploaded some images of our church and would prefer those images to be used if possible. Any stock photos used should not include any people in the photos (scenery, nature, buildings, animals, etc. are fine).

The site will need 4 pages: Home, Support Us (Donate), Login, and Recording Library.

Page 1: Home
The home page should include the following sections:

- Navigation: Should include links to each section of the home page plus a "listen live" link which will take the user to a live-streaming site and a "support us" link which will take the user to a support/donate page.

- Announcements: Can be either a banner or some other design, but there needs to be some way for us to post announcements for visitors to see. I'm open for creative ideas in this section, but would like it not to take up a lot of room on the page.

- About Us: Should include address, service times (see attached document), and information about the church.

- Pastor Bio: A section that introduces our pastor and gives a short bio about our pastor. Would like this section to include a picture of our pastor. Somewhere in this section I would like to include this Bible reference: "And I will give you pastors according to mine heart, which shall feed you with knowledge and understanding. Jer 3:15 KJV"

- Articles of Faith (What We Believe): This should include several sub-sections each with a heading, body, and possibly 1 or more scripture references. I have attached a document to the brief that includes our articles of faith. Feel free to be creative with this section in how you lay these out and format them.

- Support Us: A small section that explains what kind of support someone can give and a link to a donation page. The link can say something like "Support Us" or "Donate Now".

- Contact form: A contact form that allows the visitor to send us a message. The contact form should ask for name, email, phone, and message.

- Footer: A footer that will be displayed on all pages of the site. This should include at a minimum a link to the home page (or a link to each individual section in the home page if you prefer), a link to "listen live", a link to "support us", a link to "contact us" (or you can put the contact form directly in the footer if you prefer), the address, and a "member login" link.

Page 2: Support Us
The donation page should include a form the visitor can fill out to make a donation. We will embed a third party form later. For this design, please just mock out the design with a basic form asking for name, phone, and email.

Page 3: Login
The recording library (detailed below) will require members to login with a shared numeric code before accessing the page. We need a design for a login screen. The screen should include navigation/footer just like all other pages, but the body of the login page will consist only of a form that asks the user to enter the access code and then a "login" button.

Page 4: Recording Library

The library page is a member-only page that will require a shared, numeric pass code to access. On this page, members will be able to access a filterable list of past sermons. The page by default should display most recent sermons, but should also include a search form that allows the member to filter the sermon list to find a particular sermon. The search form should allow the user to select a filter type (e.g. Speaker name, date, event, etc.) and type in a value to search. They should be able to add multiple filters and remove filters that have been added. Each sermon that is displayed in the result list should include basic information such as title, date, speaker, tags, etc. along with a download icon, and an embedded audio player where they can click a play button to stream it on-demand. Each sermon should also have clickable tags associated with it that can be used to find related sermons.
Updates

I have uploaded several images of our church. Feel free to incorporate these into your design if possible.

Target Market(s)

Church Members

Industry/Entity Type

Religion

Number of Pages Required

4 page

Font styles to use
Sans Serif

Colors

Designer to choose colors to be used in the design.

Requirements
Must have
• Must incorporate the logo (attached)
Nice to have
• Would like the design to incorporate pictures of our church (attached) instead of stock photos if possible.
Should not have
• Please avoid an overly cluttered design. Stock photos used should not include any people in the photos.

```html
<!DOCTYPE html>
<html lang="en">
<head>
<meta charset="utf-8">
<title>Cedar Grove Chapel — Home</title>
<link rel="stylesheet" href="https://fonts.googleapis.com/css2?family=Outfit:wght@300;400;500;600;700;800;900&family=Allura&display=swap">
<style>
:root{
  --ink:#1c1b1a;
  --text:#2a2927;
  --muted:#555;
  --teal:#17bdd6;
  --teal-dark:#12adc6;
  --green:#7fcb6c;
  --red:#ef4a5a;
  --paper:#ffffff;
  --soft:#f7f5f7;
  --footer:#201f1d;
  --footer-text:#e9e9e9;
  --field:#2e2d2b;
  --field-line:#4a4946;
}
*{box-sizing:border-box;margin:0;padding:0}
html,body{width:1200px;height:2852px;overflow:hidden}
body{position:relative;background:var(--paper);font-family:"Outfit",sans-serif;color:var(--text)}
.abs{position:absolute}

/* header */
.site-header{left:0;top:0;width:1200px;height:75px;background:var(--paper)}
.brand{left:77px;top:22px;display:flex;align-items:center;gap:10px;font-weight:500;font-size:21px;color:var(--teal-dark);letter-spacing:.5px}
.brand-mark{width:22px;height:22px;border:2px solid var(--teal-dark)}
.main-nav{right:78px;top:29px;display:flex;gap:34px;font-size:15px;font-weight:600;color:var(--ink)}
.main-nav a{color:inherit;text-decoration:none}
.main-nav .live{color:var(--teal-dark)}

/* hero */
.hero{left:0;top:75px;width:1200px;height:401px;background:var(--paper);box-shadow:0 6px 10px rgba(0,0,0,.05)}
.hero-photo{left:300px;top:0;width:900px;height:401px;background:linear-gradient(90deg,#fff 0%,rgba(255,255,255,.6) 18%,rgba(243,226,210,.7) 40%,#f6ebe0 60%,#e9cdb4 100%)}
.hero-title{left:111px;top:33px;font-size:51px;font-weight:800;line-height:64px;color:var(--ink)}
.hero-sub{left:111px;top:176px;font-size:28px;font-weight:600;color:var(--ink)}
.hero-copy{left:111px;top:228px;width:460px;font-size:21px;font-weight:400;line-height:27px;color:var(--ink)}
.btn{display:flex;align-items:center;justify-content:center;background:var(--teal);color:#fff;font-weight:800;border-radius:30px;text-decoration:none;box-shadow:0 14px 20px rgba(23,189,214,.18)}
.btn-join{left:111px;top:301px;width:180px;height:60px;font-size:24px}

/* welcome / about */
.welcome-title{left:200px;top:515px;font-family:"Allura",cursive;font-size:60px;color:var(--ink);font-weight:400}
.welcome-copy{left:223px;top:640px;width:775px;font-size:25px;font-weight:300;line-height:30px;letter-spacing:.35px;text-align:justify;color:var(--ink)}
.welcome-address{left:223px;top:803px;display:flex;align-items:center;gap:8px;font-size:18px;font-weight:400;color:var(--muted)}
.btn-more{left:223px;top:849px;width:278px;height:59px;font-size:19px;border-radius:14px;gap:8px}

/* beliefs */
.beliefs{left:0;top:951px;width:1200px;height:475px;background:linear-gradient(180deg,#ececeb 0%,#e4e1de 45%,#d9cdc2 75%,#cbb7a5 100%)}
.beliefs-kicker{left:0;top:39px;width:1200px;text-align:center;font-size:23px;font-weight:600;color:var(--ink)}
.beliefs-title{left:0;top:104px;width:1200px;text-align:center;font-size:60px;font-weight:800;color:var(--ink)}
.beliefs-copy{left:160px;top:214px;width:880px;text-align:center;font-size:29px;font-weight:300;line-height:36px;color:var(--ink)}
.dots{left:487px;top:400px;display:flex;gap:16px;align-items:center}
.dot{width:12px;height:12px;border-radius:50%;background:#fff}
.dot.active{width:20px;height:20px;background:#000}

/* pastor */
.pastor-photo{left:145px;top:1460px;width:315px;height:442px;background:linear-gradient(180deg,#f2f2f2 0%,#e4e4e6 60%,#d8d8dc 100%);border-radius:140px 140px 0 0}
.pastor-kicker{left:551px;top:1508px;font-size:14px;font-weight:500;color:var(--muted)}
.pastor-ref{left:551px;top:1556px;font-size:39px;font-weight:700;color:var(--ink)}
.pastor-quote{left:551px;top:1635px;width:505px;font-size:30px;font-weight:600;line-height:37px;color:var(--ink)}
.pastor-bio{left:551px;top:1784px;width:510px;font-size:25px;font-weight:300;line-height:30px;color:var(--ink)}

/* services */
.services-band{left:0;top:1902px;width:1200px;height:478px;background:var(--soft)}
.service-title{left:184px;top:1972px;width:400px;text-align:center;font-size:29px;font-weight:800;color:var(--ink)}
.service-list{left:184px;top:2050px;width:420px;text-align:center;font-size:24px;line-height:31px;color:var(--ink)}
.service-list dt{font-weight:600}
.service-list dd{font-weight:300}
.announce-title{left:625px;top:1966px;width:370px;display:flex;justify-content:center;align-items:center;gap:10px;font-size:29px;font-weight:800;color:var(--ink)}
.announce-card{left:625px;top:2023px;width:369px;height:279px;border-radius:22px;background:linear-gradient(180deg,var(--teal) 0%,var(--green) 100%);display:flex;align-items:center;justify-content:center;text-align:center;padding:0 44px 20px;color:#fff;font-size:24px;font-weight:600;line-height:31px}
.announce-card strong{font-weight:800}

/* donate + footer */
.site-footer{left:0;top:2380px;width:1200px;height:472px;background:var(--footer);color:var(--footer-text)}
.btn-donate{left:495px;top:2357px;width:210px;height:49px;background:var(--red);border-radius:26px;color:#fff;font-size:19px;font-weight:600;display:flex;align-items:center;justify-content:center;gap:8px;text-decoration:none}
.footer-col{top:85px}
.footer-col h4{font-size:19px;font-weight:800;color:#fff;margin-bottom:22px}
.footer-col li{list-style:none;font-size:19px;font-weight:300;margin-bottom:25px}
.footer-col p{font-size:19px;font-weight:300;line-height:24px}
.footer-col .email{display:block;margin:16px 0 20px;color:#fff;text-decoration:underline;font-size:19px;font-weight:300}
.socials{display:flex;gap:26px}
.socials span{width:40px;height:40px;border-radius:50%;background:#fff}

.contact-form{left:900px;top:85px;width:230px}
.contact-form h4{margin-bottom:16px}
.field{display:block;width:100%;height:32px;margin-bottom:8px;padding:0 10px;border:1px solid var(--field-line);border-radius:6px;background:var(--field);color:#bbb;font-family:"Outfit",sans-serif;font-size:14px;font-weight:300;line-height:30px}
.field.message{height:58px}
.btn-send{width:100%;height:34px;border:0;border-radius:17px;background:var(--teal);color:#fff;font-family:"Outfit",sans-serif;font-size:15px;font-weight:700}

.copyright{left:83px;top:409px;font-size:19px;font-weight:300}
.copyright a{color:var(--teal);text-decoration:underline}
</style>
</head>
<body>

<header class="site-header abs">
  <div class="brand abs"><span class="brand-mark"></span>Cedar Grove Chapel</div>
  <nav class="main-nav abs"><a class="live" href="#">Listen Live</a><a href="#">Get Involved</a><a href="#">About Us</a><a href="#">Log in</a></nav>
</header>

<section class="hero abs">
  <div class="hero-photo abs" role="img" aria-label="Bright church interior with tall arched windows"></div>
  <h1 class="hero-title abs">LOVE GOD<br>&amp; LOVE LIFE!</h1>
  <p class="hero-sub abs">Join our Live Sermons.</p>
  <p class="hero-copy abs">Make your day more fulfilling with a variety of sermons from different speakers.</p>
  <a class="btn btn-join abs" href="#">JOIN NOW</a>
</section>

<h2 class="welcome-title abs">Giving You a Warm Welcome!</h2>
<p class="welcome-copy abs">Our mission is helping people find their way back to God. We accomplish this by reaching people far from God, restoring God’s dream for the world, and reproducing this mission in others. There are three key relationships that help you develop a growing relationship with Jesus.</p>
<p class="welcome-address abs">
  <svg width="16" height="20" viewBox="0 0 16 20" fill="none" stroke="#555" stroke-width="1.8"><path d="M8 19s6-6.2 6-11A6 6 0 0 0 2 8c0 4.8 6 11 6 11z"/><circle cx="8" cy="8" r="2.2"/></svg>
  Maple Ridge Rd, Fairview Springs, Ohio(OH), 45001
</p>
<a class="btn btn-more abs" href="#">KNOW MORE ABOUT US
  <svg width="16" height="16" viewBox="0 0 16 16" fill="none" stroke="#fff" stroke-width="2.2" stroke-linecap="round" stroke-linejoin="round"><path d="M2 8h11M9 4l4 4-4 4"/></svg>
</a>

<section class="beliefs abs" role="img" aria-label="Faded photo of the brick church building">
  <p class="beliefs-kicker abs">WHAT WE BELIEVE</p>
  <h2 class="beliefs-title abs">THE GOD HEAD</h2>
  <p class="beliefs-copy abs">We believe in the God head bodily, known as the Divine Trinity. This body consist of God the father, Jesus Christ, his only begotten son and the redeemer of the world, and of the Holy Ghost, The third person of the Divine Trinity.</p>
  <div class="dots abs"><span class="dot active"></span><span class="dot"></span><span class="dot"></span><span class="dot"></span><span class="dot"></span><span class="dot"></span><span class="dot"></span></div>
</section>

<div class="pastor-photo abs" role="img" aria-label="Portrait of the pastor"></div>
<p class="pastor-kicker abs">SOMETHING TO KNOW</p>
<h2 class="pastor-ref abs">Jer 3:15 KJV</h2>
<blockquote class="pastor-quote abs">“And I will give you pastors according to mine heart, which shall feed you with knowledge and understanding.”</blockquote>
<p class="pastor-bio abs">A section that introduces our pastor and gives a short bio about our pastor. Would like this section to include a picture of our pastor.</p>

<div class="services-band abs"></div>
<h2 class="service-title abs">TIME OF SERVICE</h2>
<dl class="service-list abs">
  <dt>Wednesday Evening Service</dt><dd>7:30 PM</dd>
  <dt>Sunday School</dt><dd>10:00 AM</dd>
  <dt>Sunday Morning Service</dt><dd>11:00 AM</dd>
  <dt>Sunday Evening Service</dt><dd>5:30 PM</dd>
</dl>
<h2 class="announce-title abs">ANNOUNCEMENT
  <svg width="24" height="24" viewBox="0 0 24 24" fill="none" stroke="#1c1b1a" stroke-width="2.2" stroke-linejoin="round"><path d="M3 3h18v14H9l-4 4v-4H3z"/><path d="M8 10h.01M12 10h.01M16 10h.01" stroke-linecap="round" stroke-width="2.8"/></svg>
</h2>
<div class="announce-card abs"><p>Be reminded that we will be having a Sunday Sermon with Pastor this coming <strong>FEBUARY 30, 2023 at 9:00 PM.</strong></p></div>

<footer class="site-footer abs">
  <div class="footer-col abs" style="left:83px"><h4>WHO WE ARE</h4><ul><li>About us</li><li>Ministries</li><li>Events</li></ul></div>
  <div class="footer-col abs" style="left:275px"><h4>INFO</h4><ul><li>Careers</li><li>Community</li><li>Blog</li><li>Press</li></ul></div>
  <div class="footer-col abs" style="left:417px"><h4>HELP</h4><ul><li>Contact us</li><li>FAQ</li><li>Legal &amp; Privacy</li></ul></div>
  <div class="footer-col abs" style="left:594px;width:270px">
    <h4>FIND US AT</h4>
    <p>(555) 014-2290<br>Maple Ridge Rd, Fairview Springs, Ohio(OH), 45001</p>
    <h4 style="margin:12px 0 0">WRITE TO US</h4>
    <a class="email" href="#">hello@cedargrovechapel.org</a>
    <div class="socials"><span></span><span></span><span></span><span></span></div>
  </div>
  <form class="contact-form footer-col abs">
    <h4>CONTACT US</h4>
    <div class="field">Name</div>
    <div class="field">Email</div>
    <div class="field">Phone</div>
    <div class="field message">Message</div>
    <button class="btn-send" type="button">SEND MESSAGE</button>
  </form>
  <p class="copyright abs">© 2021 Cedar Grove. All Rights Reserved. <a href="#">Privacy Policy</a></p>
</footer>

<a class="btn-donate abs" href="#">
  <svg width="30" height="28" viewBox="0 0 24 22"><path fill="#fff" d="M12 21S1 14 1 7a5.5 5.5 0 0 1 11-1 5.5 5.5 0 0 1 11 1c0 7-11 14-11 14z"/></svg>
  DONATE NOW
</a>

</body>
</html>
```